TUL Mission & Values Poster design

The company has developed a new Mission/Purpose statement and new core values which we want to communicate broadly. We are looking for an engaging poster design which illustrates the importance of the values.

An extract of the presentation to announce the update to mission and values as well as an extract of the new hire orientation are attached for reference regarding the company. Also attaching the company logo file for your use/reference.

Target Market(s)

Employees

Industry/Entity Type

Energy

Requirements
Must have
• Logo and brand consistency, engaging messaging and imagery
Should not have
• Wind or Oil industry imagery or references

```html
<!DOCTYPE html>
<html lang="en">
<head>
<meta charset="utf-8">
<title>TUL-Rochester Mission &amp; Core Values</title>
<link href="https://fonts.googleapis.com/css2?family=Archivo:wght@700;800;900&family=Hind:wght@400;500&display=swap" rel="stylesheet">
<style>
  :root {
    --paper: #fdf4ea;
    --page-bg: #f4f4f2;
    --brand-green: #4f8726;
    --brand-red: #d21f30;
    --sky: #cfe5e4;
    --foliage: #3f7f2a;
    --ink: #1c1c1c;
  }
  * { margin: 0; padding: 0; box-sizing: border-box; }
  html, body { width: 1200px; height: 1200px; overflow: hidden; }
  body { background: var(--page-bg); position: relative; font-family: "Hind", sans-serif; }

  .poster {
    position: absolute; left: 222px; top: 34px;
    width: 755px; height: 1131px;
    background: var(--paper);
    overflow: hidden;
  }

  .brand-mark {
    position: absolute; left: 50px; top: 130px;
    display: flex; align-items: center; gap: 7px;
    font-family: "Archivo", sans-serif; font-weight: 800;
    font-size: 18px; line-height: 24px; color: var(--brand-red); letter-spacing: -0.3px;
  }
  .brand-mark .dot {
    width: 15px; height: 15px; border-radius: 50%;
    background: var(--brand-green);
  }

  .mission-title {
    position: absolute; left: 240px; top: 24px;
    font-family: "Archivo", sans-serif; font-weight: 900;
    font-size: 104px; line-height: 1; color: var(--brand-green);
    letter-spacing: -1px;
  }

  .mission-statement {
    position: absolute; left: 77px; top: 164px; width: 620px;
    font-family: "Archivo", sans-serif; font-weight: 800;
    font-size: 52px; line-height: 58px; color: var(--brand-red);
    letter-spacing: -0.6px;
    z-index: 2;
  }

  .scene {
    position: absolute; left: 0; top: 345px;
    width: 755px; height: 325px;
    background:
      linear-gradient(180deg, var(--paper) 0%, var(--sky) 18%, #d7e8df 45%, #6a9a3a 80%, var(--foliage) 100%);
  }

  .values-band {
    position: absolute; left: 0; top: 670px;
    width: 755px; height: 80px;
    background: var(--brand-green);
    display: flex; align-items: center; justify-content: center;
    font-family: "Archivo", sans-serif; font-weight: 900;
    font-size: 58px; line-height: 1; color: var(--paper); letter-spacing: 1px;
  }

  .value-icon { position: absolute; width: 74px; height: 74px; }
  .value-copy { position: absolute; width: 265px; }
  .value-name {
    font-family: "Archivo", sans-serif; font-weight: 900;
    font-size: 36px; line-height: 40px; color: var(--brand-red);
  }
  .value-text {
    font-size: 25px; line-height: 30px; color: var(--ink);
    margin-top: 0;
  }

  .safety .value-icon    { left: 46px;  top: 772px; }
  .safety .value-copy    { left: 131px; top: 765px; }
  .integrity .value-icon { left: 395px; top: 772px; }
  .integrity .value-copy { left: 472px; top: 765px; }
  .team .value-icon      { left: 46px;  top: 898px; }
  .team .value-copy      { left: 131px; top: 888px; }
  .service .value-icon   { left: 395px; top: 896px; }
  .service .value-copy   { left: 472px; top: 888px; }

  .footer-name {
    position: absolute; left: 0; right: 0; top: 1030px;
    text-align: center;
    font-family: "Archivo", sans-serif; font-weight: 900;
    font-size: 68px; line-height: 1.1; color: var(--brand-green); letter-spacing: -1px;
  }
</style>
</head>
<body>
  <main class="poster">
    <div class="brand-mark"><span class="dot"></span>TUL-Rochester</div>
    <h1 class="mission-title">MISSION</h1>
    <p class="mission-statement">To provide innovative energy solutions for our community.</p>

    <div class="scene" role="img" aria-label="Illustration of two workers in hard hats shaking hands in front of an energy plant with chimneys, trees and a city skyline"></div>

    <h2 class="values-band">CORE VALUES</h2>

    <section class="value safety">
      <svg class="value-icon" viewBox="0 0 80 80" aria-hidden="true">
        <path d="M40 6 L77 70 Q78 74 74 74 H6 Q2 74 3 70 Z" fill="var(--brand-red)" stroke="var(--brand-red)" stroke-linejoin="round" stroke-width="4"/>
        <rect x="36" y="28" width="8" height="26" rx="4" fill="var(--paper)"/>
        <circle cx="40" cy="63" r="4.5" fill="var(--paper)"/>
      </svg>
      <div class="value-copy">
        <h3 class="value-name">SAFETY</h3>
        <p class="value-text">We put safety first<br>at all times.</p>
      </div>
    </section>

    <section class="value integrity">
      <svg class="value-icon" viewBox="0 0 80 80" aria-hidden="true">
        <circle cx="40" cy="40" r="35" fill="var(--brand-red)"/>
        <path d="M24 41 L35 52 L57 29" fill="none" stroke="var(--paper)" stroke-width="8" stroke-linecap="round" stroke-linejoin="round"/>
      </svg>
      <div class="value-copy">
        <h3 class="value-name">INTEGRITY</h3>
        <p class="value-text">We uphold the highest<br>standards of integrity.</p>
      </div>
    </section>

    <section class="value team">
      <svg class="value-icon" viewBox="0 0 80 80" aria-hidden="true">
        <circle cx="18" cy="18" r="9" fill="var(--brand-red)"/>
        <circle cx="62" cy="18" r="9" fill="var(--brand-red)"/>
        <path d="M2 50 Q2 30 18 30 Q30 30 32 40 L32 50 Z" fill="var(--brand-red)"/>
        <path d="M78 50 Q78 30 62 30 Q50 30 48 40 L48 50 Z" fill="var(--brand-red)"/>
        <circle cx="40" cy="34" r="11" fill="var(--brand-red)" stroke="var(--paper)" stroke-width="3"/>
        <path d="M18 76 Q18 50 40 50 Q62 50 62 76 Z" fill="var(--brand-red)" stroke="var(--paper)" stroke-width="3"/>
      </svg>
      <div class="value-copy">
        <h3 class="value-name">TEAM</h3>
        <p class="value-text">We succeed together<br>through teamwork<br>and collaboration.</p>
      </div>
    </section>

    <section class="value service">
      <svg class="value-icon" viewBox="0 0 80 80" aria-hidden="true">
        <path d="M40 74 C20 56 4 44 4 26 C4 14 13 6 23 6 C31 6 37 10 40 17 C43 10 49 6 57 6 C67 6 76 14 76 26 C76 44 60 56 40 74 Z" fill="var(--brand-red)"/>
      </svg>
      <div class="value-copy">
        <h3 class="value-name">SERVICE</h3>
        <p class="value-text">We provide reliable<br>service to all our<br>customers.</p>
      </div>
    </section>

    <p class="footer-name">TUL-Rochester</p>
  </main>
</body>
</html>
```